Actors Postcard Design

I need a postcard designed for me. I am an actor, voice over artist and technical adviser for tv, film and videogames. I am open to color ideas. My photos are in black and white so something to make those stand out a bit. Masculine colors like dark blue etc..I have seen some of your designs with 3 photos which I liked. Perhaps a 2-3 photo scheme. Back of postcard to contain my resume. Want it to look professional and not cartoonish (since I mentioned video games). Front to have photos and job title and contact info

Please take my color direction lightly, I am open to all color schemes. light or dark. You are the professionals. Am looking forward to seeing what all of you come up with. Thanks

Tv

```html
<!DOCTYPE html>
<html lang="en">
<head>
<meta charset="utf-8">
<title>Tomasz “Tom” Kowalczyk – Actor Postcard</title>
<link rel="stylesheet" href="https://fonts.googleapis.com/css2?family=Roboto+Condensed:wght@700&family=Roboto:wght@300&family=Parisienne&display=swap">
<style>
  :root {
    --navy: #0b2f86;
    --blue: #1a64c8;
    --blue-bright: #2a86e0;
    --cyan: #3ee4e6;
    --orange: #ffb400;
    --green: #66f01e;
    --teal: #48e3d6;
    --yellow: #f5c81a;
    --white: #ffffff;
    --silver: #d9dde2;
  }
  * { margin: 0; padding: 0; box-sizing: border-box; }
  html, body { width: 1200px; height: 923px; overflow: hidden; background: #ffffff; }
  .postcard { position: relative; width: 1200px; height: 923px; overflow: hidden; }
  .backdrop { position: absolute; inset: 0; }

  .roles { position: absolute; left: 0; top: 487px; list-style: none; }
  .role {
    display: block; height: 53px; margin-bottom: 16px;
    padding-left: 52px;
    font-family: "Roboto Condensed", "Arial Narrow", sans-serif;
    font-weight: 700; font-size: 42px; line-height: 55px; letter-spacing: 0.4px;
    color: var(--white); white-space: nowrap;
  }
  .role--actor { width: 207px; background: var(--orange); }
  .role--voice { width: 383px; background: var(--green); }
  .role--advisor { width: 440px; background: var(--teal); }

  .tagline {
    position: absolute; left: 182px; top: 694px;
    font-family: "Parisienne", cursive;
    font-size: 44px; color: var(--white); white-space: nowrap;
  }

  .contact { position: absolute; left: 0; top: 805px; width: 1200px; height: 90px; }
  .contact__name {
    position: absolute; left: 90px; top: 20px;
    font-family: "Roboto Condensed", "Arial Narrow", sans-serif;
    font-weight: 700; font-size: 50px; letter-spacing: 0.6px;
    color: var(--cyan); white-space: nowrap;
  }
  .contact__divider {
    position: absolute; left: 716px; top: 0; width: 2px; height: 88px;
    background: var(--white);
  }
  .contact__phone {
    position: absolute; left: 738px; top: -4px;
    font-family: "Roboto", Arial, sans-serif;
    font-weight: 300; font-size: 71px;
    color: var(--yellow); white-space: nowrap;
  }
</style>
</head>
<body>
<main class="postcard">
  <svg class="backdrop" width="1200" height="923" viewBox="0 0 1200 923" xmlns="http://www.w3.org/2000/svg">
    <defs>
      <linearGradient id="sky" x1="0" y1="0" x2="0" y2="1">
        <stop offset="0" stop-color="#eceeef"/>
        <stop offset="1" stop-color="#d2d5d8"/>
      </linearGradient>
      <linearGradient id="column-gold" x1="0" y1="0" x2="0" y2="1">
        <stop offset="0" stop-color="#e9e592"/>
        <stop offset="1" stop-color="#d2ca74"/>
      </linearGradient>
      <linearGradient id="column-tan" x1="0" y1="0" x2="0" y2="1">
        <stop offset="0" stop-color="#7d6a50"/>
        <stop offset="1" stop-color="#b3a07c"/>
      </linearGradient>
      <linearGradient id="column-teal" x1="0" y1="0" x2="0" y2="1">
        <stop offset="0" stop-color="#3e9fd0"/>
        <stop offset="1" stop-color="#2a78c4"/>
      </linearGradient>
      <radialGradient id="headshot-cyan" cx="0.5" cy="0.45" r="0.62">
        <stop offset="0" stop-color="#9fe6ef"/>
        <stop offset="0.55" stop-color="#6cc8d6"/>
        <stop offset="1" stop-color="#2f7f92"/>
      </radialGradient>
      <radialGradient id="headshot-sepia" cx="0.5" cy="0.5" r="0.6">
        <stop offset="0" stop-color="#b9a98a"/>
        <stop offset="0.5" stop-color="#7f6f55"/>
        <stop offset="1" stop-color="#3f3526"/>
      </radialGradient>
      <linearGradient id="sepia-shirt" x1="0" y1="0" x2="0" y2="1">
        <stop offset="0" stop-color="#6b5d47" stop-opacity="0"/>
        <stop offset="1" stop-color="#5a4c38"/>
      </linearGradient>
      <radialGradient id="portrait-main" cx="0.52" cy="0.38" r="0.62">
        <stop offset="0" stop-color="#e4e4e4"/>
        <stop offset="0.45" stop-color="#b8b8b8"/>
        <stop offset="0.8" stop-color="#9a9a9a"/>
        <stop offset="1" stop-color="#c9c9c9"/>
      </radialGradient>
      <linearGradient id="portrait-jacket" x1="0" y1="0" x2="0" y2="1">
        <stop offset="0" stop-color="#3a3a3a" stop-opacity="0"/>
        <stop offset="0.5" stop-color="#333333" stop-opacity="0.75"/>
        <stop offset="1" stop-color="#2a2a2a" stop-opacity="0.9"/>
      </linearGradient>
      <linearGradient id="sea" x1="0" y1="0" x2="0.3" y2="1">
        <stop offset="0" stop-color="var(--blue-bright)"/>
        <stop offset="0.45" stop-color="var(--blue)"/>
        <stop offset="1" stop-color="var(--navy)"/>
      </linearGradient>
      <linearGradient id="chrome" x1="0" y1="0" x2="0" y2="1">
        <stop offset="0" stop-color="#ffffff"/>
        <stop offset="0.5" stop-color="var(--silver)"/>
        <stop offset="1" stop-color="#9aa2ab"/>
      </linearGradient>
    </defs>

    <rect class="sky" width="1200" height="923" fill="url(#sky)"/>

    <!-- first photo column -->
    <rect x="70" y="0" width="255" height="47" fill="#a8e2ea"/>
    <g role="img" aria-label="Cyan-toned close-up headshot of the actor, smiling">
      <rect x="70" y="47" width="255" height="253" fill="url(#headshot-cyan)"/>
    </g>
    <rect x="70" y="300" width="255" height="200" fill="url(#column-teal)"/>

    <!-- second photo column -->
    <rect x="325" y="0" width="255" height="185" fill="url(#column-gold)"/>
    <g role="img" aria-label="Sepia photo of the actor in a plaid shirt in front of trees">
      <rect x="325" y="185" width="255" height="253" fill="url(#headshot-sepia)"/>
      <rect x="325" y="360" width="255" height="78" fill="url(#sepia-shirt)"/>
    </g>
    <rect x="325" y="438" width="255" height="200" fill="url(#column-tan)"/>

    <!-- main portrait -->
    <g role="img" aria-label="Large black and white portrait of the actor in a dark jacket">
      <polygon points="580,0 1200,0 1200,545 890,785 580,600" fill="url(#portrait-main)"/>
      <polygon points="620,480 1160,480 1200,545 890,785 620,625" fill="url(#portrait-jacket)"/>
    </g>

    <!-- blue field with chrome edge -->
    <polygon points="0,278 890,808 1200,568 1200,923 0,923" fill="url(#sea)"/>
    <polygon points="0,244 890,783 1200,543 1200,566 890,806 0,276" fill="url(#chrome)"/>
    <polyline points="0,284 890,812 1200,572" fill="none" stroke="var(--cyan)" stroke-width="3"/>
  </svg>

  <ul class="roles">
    <li class="role role--actor">Actor</li>
    <li class="role role--voice">Voice over artist</li>
    <li class="role role--advisor">Technical adviser</li>
  </ul>

  <p class="tagline">…for tv, film and videogames</p>

  <div class="contact">
    <p class="contact__name">TOMASZ “TOM” KOWALCZYK</p>
    <span class="contact__divider"></span>
    <p class="contact__phone">503-555-0142</p>
  </div>
</main>
</body>
</html>
```